Recruitment Web Site Design

I need a Recruitment website explaining who we are and what services we deliver.
This is a new company and the image we portray is extremely important. Must be very professional.
Our target marget are bluechip companies and professionals including executives.

The final design should communicate connecting professionals matching company and individual needs.

Target Market(s)

Corporate, Blue Chip Companies, Professionals/Executives

Industry/Entity Type

It Company

Requirements
Must have
• Must be professional and Sophisticated.
Must have a few tabs.

Must be unique to the norm of websites as I am looking for something different.
Nice to have
• Good graphics with people connecting. Multi - racial pics will be good as we are in South Africa and diversity is a must.
Also a front page (be unique).

I am putting this out there for you to use your imagination and come up with something brilliant.

A few websites you can base ideas from

www.maplevertex.com
www.thestaffnook.co.za
www.kvt.co.za
www.rul.co.za

```html
<!DOCTYPE html>
<html lang="en">
<head>
<meta charset="utf-8">
<title>Taviro Recruitment</title>
<link rel="stylesheet" href="https://fonts.googleapis.com/css2?family=PT+Sans:wght@400;700&family=Didact+Gothic&family=Cinzel:wght@400&family=Tinos&display=swap">
<style>
  :root {
    --page: #dadada;
    --page-light: #e9e9e9;
    --white: #ffffff;
    --ink: #2a2a2a;
    --ink-soft: #555555;
    --hero-light: #d2d2d2;
    --hero-dark: #808080;
    --photo-dark: #2b2522;
    --photo-mid: #4d4039;
    --photo-warm: #6b5a4e;
    --map-tone: #666666;
    --brand-red: #c4121a;
    --brand-dark: #3a3a3a;
    --card-top: #cfcfcf;
    --card-bottom: #f2f2f2;
    --social: #4a8fc7;
    --footer-dark: #8a8a8a;
  }
  * { box-sizing: border-box; margin: 0; padding: 0; }
  html, body { width: 1200px; height: 900px; overflow: hidden; }
  body {
    position: relative;
    background: linear-gradient(180deg, var(--page-light) 0%, var(--page) 55%, var(--page-light) 85%);
    font-family: "PT Sans", sans-serif;
    color: var(--ink);
  }

  .site-header {
    position: absolute; left: 0; top: 7px; width: 1195px; height: 56px;
    background: var(--white);
  }
  .brand { position: absolute; left: 24px; top: 7px; display: flex; align-items: center; gap: 16px; }
  .brand-mark { width: 46px; height: 46px; background: var(--brand-red); }
  .brand-name { font-family: "Cinzel", serif; font-size: 22px; letter-spacing: 4px; color: var(--brand-dark); }
  .main-nav a { position: absolute; top: 16px; font-size: 20px; color: var(--ink); text-decoration: none; }
  .nav-home { left: 686px; } .nav-services { left: 793px; }
  .nav-about { left: 906px; } .nav-contact { left: 1022px; }

  .hero {
    position: absolute; left: 0; top: 80px; width: 1195px; height: 349px;
    background: linear-gradient(180deg, var(--hero-light) 0%, #b4b4b4 38%, #939393 42%, var(--hero-dark) 100%);
    overflow: hidden;
  }
  .hero-photo {
    position: absolute; left: 0; top: 0; width: 440px; height: 349px;
    background:
      linear-gradient(90deg, var(--photo-dark) 0%, var(--photo-mid) 45%, var(--photo-warm) 72%, rgba(107,90,78,0) 100%);
    -webkit-mask-image: linear-gradient(180deg, rgba(0,0,0,0) 0%, #000 22%);
            mask-image: linear-gradient(180deg, rgba(0,0,0,0) 0%, #000 22%);
  }
  .hero-map {
    position: absolute; left: 680px; top: 88px; width: 433px; height: 219px;
    background: var(--map-tone); opacity: 0.45; border-radius: 40px;
  }
  .hero-title {
    position: absolute; left: 707px; top: 112px;
    font-family: "PT Sans", sans-serif; font-weight: 400; font-size: 29px; line-height: 37px; color: var(--white);
  }
  .hero-title .sub { display: block; margin-left: -7px; color: #dedede; }
  .hero-tagline { position: absolute; left: 707px; top: 195px; font-size: 19px; font-weight: 700; color: var(--white); letter-spacing: -0.2px; }
  .read-more {
    position: absolute; left: 705px; top: 233px; width: 107px; height: 37px;
    background: linear-gradient(180deg, #f4f4f4, #bdbdbd);
    box-shadow: 0 3px 6px rgba(0,0,0,0.45);
    font-weight: 700; font-size: 19px; color: #555;
    display: flex; align-items: center; justify-content: center;
  }
  .hero-shadow {
    position: absolute; left: 140px; top: 432px; width: 1000px; height: 34px;
    background: radial-gradient(ellipse at center, rgba(0,0,0,0.28) 0%, rgba(0,0,0,0) 70%);
  }

  .welcome { position: absolute; left: 36px; top: 499px; width: 265px; }
  .welcome h1 { font-family: "Tinos", serif; font-weight: 400; font-size: 17px; line-height: 20px; color: var(--brand-red); }
  .welcome p { font-size: 11px; line-height: 12.7px; color: var(--ink-soft); }

  .card {
    position: absolute; width: 165px; padding: 14px 8px 10px;
    background: linear-gradient(180deg, var(--card-top) 0%, var(--card-bottom) 28%, var(--card-bottom) 100%);
    box-shadow: 0 8px 8px -6px rgba(0,0,0,0.45);
  }
  .card h2 { font-weight: 700; font-size: 13px; color: var(--brand-red); text-align: center; margin-bottom: 14px; }
  .card p { font-family: "Didact Gothic", sans-serif; font-size: 10px; line-height: 12.6px; color: var(--ink-soft); }
  .card-outsourcing { left: 369px; top: 496px; height: 168px; }
  .card-vacancies { left: 580px; top: 496px; height: 168px; padding-top: 8px; }
  .card-why { left: 795px; top: 496px; height: 168px; }
  .card-news { left: 1008px; top: 472px; height: 238px; padding-top: 14px; }
  .card-news h2 { font-weight: 400; margin-bottom: 14px; }

  .social { position: absolute; left: 1060px; top: 763px; display: flex; gap: 11px; }
  .social a { width: 31px; height: 30px; background: var(--social); border-radius: 4px; display: block; }
  .social-shadow {
    position: absolute; left: 1055px; top: 797px; width: 125px; height: 10px;
    background: radial-gradient(ellipse at center, rgba(0,0,0,0.3), rgba(0,0,0,0) 70%);
  }

  .site-footer {
    position: absolute; left: 0; top: 795px; width: 1200px; height: 105px;
    background: linear-gradient(180deg, #bdbdbd 0%, var(--page-light) 35%, #c8c8c8 70%, var(--footer-dark) 100%);
  }
  .site-footer p {
    position: absolute; top: 74px; width: 100%; text-align: center; padding-left: 130px;
    font-size: 16px; color: #111;
  }
</style>
</head>
<body>
  <header class="site-header">
    <div class="brand">
      <span class="brand-mark"></span>
      <span class="brand-name">TAVIRO</span>
    </div>
    <nav class="main-nav">
      <a class="nav-home" href="#">Home</a>
      <a class="nav-services" href="#">Services</a>
      <a class="nav-about" href="#">About Us</a>
      <a class="nav-contact" href="#">Contact Us</a>
    </nav>
  </header>

  <section class="hero">
    <div class="hero-photo" role="img" aria-label="Photograph of a diverse group of young professionals standing in profile"></div>
    <div class="hero-map" role="img" aria-label="Faint world map"></div>
    <h2 class="hero-title">Local Service<span class="sub">Global Impact</span></h2>
    <p class="hero-tagline">Effective and Efficient Solutions To All Your Problems</p>
    <a class="read-more">Read More</a>
  </section>
  <div class="hero-shadow"></div>

  <section class="welcome">
    <h1>Welcome</h1>
    <p>The Taviro Recruitment is South Africa's first HR Service Centre where clients &amp; customers can obtain a number of "Best of Breed" HR products and services under 1 roof. Our services are varied and cover the complete HR spectrum. With over 20 different HR services at your fingertips, sourcing quality HR products &amp; services becomes simple.<br>WE provide Flexible, Effective and efficient services to out clients which not onyl saves their time but also enhance their skills and capabilities.</p>
  </section>

  <article class="card card-outsourcing">
    <h2>HR Outsourcing</h2>
    <p>lorem ispum is a dummy text lorem ispum is a dummy textlorem ispum is a dummy text lorem ispum is a dummy text lorem ispum is a dummy text lorem ispum is a dummy text lorem ispum is a dummy text</p>
  </article>
  <article class="card card-vacancies">
    <h2>Vacancies</h2>
    <p>lorem ispum is a dummy text lorem ispum is a dummy textlorem ispum is a dummy text lorem ispum is a dummy text lorem ispum is a dummy text lorem ispum is a dummy text lorem ispum is a dummy text lorem ispum is a dummy text</p>
  </article>
  <article class="card card-why">
    <h2>Why Us</h2>
    <p>lorem ispum is a dummy text lorem ispum is a dummy textlorem ispum is a dummy text lorem ispum is a dummy text lorem ispum is a dummy text lorem ispum is a dummy text lorem ispum is a dummy text lorem ispum is a dummy text</p>
  </article>
  <article class="card card-news">
    <h2>Latest News</h2>
    <p>lorem ispum is a dummy text lorem ispum is a dummy textlorem ispum is a dummy text lorem ispum is a dummy text lorem ispum is a dummy text lorem ispum is a dummy text lorem ispum is a dummy text lorem ispum is a dummy text dummy text lorem ispum is a dummy text dummy text lorem ispum is a dummy text dummy text lorem ispum is a dummy</p>
  </article>

  <footer class="site-footer">
    <p>All Rights Reserved</p>
  </footer>
  <nav class="social" aria-label="Social links">
    <a href="#" aria-label="Social link one"></a>
    <a href="#" aria-label="Social link two"></a>
    <a href="#" aria-label="Social link three"></a>
  </nav>
  <div class="social-shadow"></div>
</body>
</html>
```